Rack Card Design for an Ayurvedic Beauty Product Project

Hello, I need to have rack cards. The rack cards would be about 3 products we are showcasing at an event. I am a cosmetic company. I have a logo and basic design ideas. I have attached some product images and info. By no means am I a designer so please excuse my messy AI files. Please feel free to design this as feminine as you like. :)

Target Market(s)

Beauty industry, organic, holistic, ayurveda

Industry/Entity Type

Cosmetic

```html
<!DOCTYPE html>
<html lang="en">
<head>
<meta charset="UTF-8">
<title>Velvet Lotus Rack Cards</title>
<link href="https://fonts.googleapis.com/css2?family=Open+Sans:wght@400;600;700&family=Great+Vibes&display=swap" rel="stylesheet">
<style>
:root{
  --plum:#560b3a;
  --plum-light:#701a4f;
  --gold:#c9a05f;
  --gold-light:#e8c98a;
  --ink:#222;
  --muted:#444;
  --paper:#fff;
  --stage:#ecebe8;
}
*{margin:0;padding:0;box-sizing:border-box}
html,body{width:1200px;height:902px;overflow:hidden}
body{background:var(--stage);font-family:"Open Sans",sans-serif;position:relative}
.rack-card{position:absolute;width:354px;height:770px;background:var(--paper);overflow:hidden;box-shadow:0 4px 14px rgba(0,0,0,.25)}
.rack-card--front{left:209px;top:50px}
.rack-card--back{left:631px;top:74px;background:linear-gradient(90deg,#d9d9d9 0%,#fff 45%,#fff 60%,#dcdcdc 100%)}
.card-shapes{position:absolute;inset:0;width:100%;height:100%}
.abs{position:absolute}

/* front */
.brand-mark{left:0;right:0;top:30px;display:flex;align-items:center;justify-content:center;gap:8px}
.brand-mark__dot{width:22px;height:22px;border-radius:50%;background:var(--gold)}
.brand-mark__name{font-weight:600;font-size:13px;letter-spacing:.5px;color:var(--gold)}
.hero-photo{left:30px;top:139px;width:300px;height:300px;border-radius:50%;
  background:radial-gradient(circle at 50% 55%,#f3e2d6 0%,#e9cfbf 45%,#f6f3f1 80%)}
.product-thumb{width:104px;height:104px;border-radius:50%;border:3px solid #fff;
  background:radial-gradient(circle,#fff 0%,#f0ecee 60%,#d9cfd5 100%)}
.about-title{left:0;right:0;top:572px;text-align:center;font-family:"Great Vibes",cursive;font-weight:400;font-size:27px;line-height:1.2;color:var(--gold-light)}
.about-text{left:20px;width:314px;top:610px;font-size:9px;line-height:1.24;color:#fff;text-align:justify}
.front-contact{left:0;right:0;top:728px;text-align:center;font-weight:700;color:var(--ink);font-size:12.5px;line-height:1.3}

/* back */
.list-title{left:0;right:0;top:24px;text-align:center;color:#fff;font-weight:700;font-size:22px;line-height:1.22}
.product-frame{width:120px;height:120px;border-radius:50%;border:2px solid var(--plum);
  background:radial-gradient(circle,#fff 0%,#f2edf0 55%,#d8c6d0 100%)}
.product-info{left:157px;width:180px}
.product-info__name{font-weight:700;font-size:13.6px;line-height:1.27;color:var(--plum)}
.product-info__desc{margin-top:6px;font-size:9.4px;line-height:1.22;color:var(--muted);text-align:justify}
.footer-brand{left:50px;top:720px;display:flex;align-items:center;gap:6px}
.footer-brand__dot{width:18px;height:18px;border-radius:50%;background:var(--gold)}
.footer-brand__name{font-weight:600;font-size:10px;color:var(--gold)}
.footer-contact{left:153px;top:692px;color:#fff;font-weight:700}
.footer-contact__cta{font-size:11.5px;color:var(--gold-light)}
.footer-contact__phone{font-size:21px;line-height:1.15}
.footer-contact__web{font-size:12px}
</style>
</head>
<body>

<section class="rack-card rack-card--front">
  <svg class="card-shapes" viewBox="0 0 354 770" aria-hidden="true">
    <defs>
      <linearGradient id="goldSweep" x1="0" x2="1">
        <stop offset="0" stop-color="#a97c3e"/><stop offset=".5" stop-color="#f0d39a"/><stop offset="1" stop-color="#a97c3e"/>
      </linearGradient>
    </defs>
    <path d="M0,78 Q177,150 354,78 L354,722 Q177,694 0,722 Z" fill="var(--plum)"/>
    <path d="M0,88 Q115,88 172,168" stroke="url(#goldSweep)" stroke-width="12" fill="none"/>
    <path d="M354,88 Q239,88 182,168" stroke="url(#goldSweep)" stroke-width="12" fill="none"/>
    <circle cx="180" cy="289" r="168" fill="url(#goldSweep)" opacity=".85"/>
    <circle cx="180" cy="289" r="160" fill="var(--plum)"/>
    <path d="M180,130 A159,159 0 0 0 90,420" stroke="#1c1c1c" stroke-width="8" fill="none"/>
    <circle cx="180" cy="289" r="153" fill="#fff"/>
    <path d="M0,722 Q177,694 354,722" stroke="url(#goldSweep)" stroke-width="3" fill="none"/>
  </svg>

  <div class="abs brand-mark"><span class="brand-mark__dot"></span><span class="brand-mark__name">VELVET LOTUS</span></div>
  <div class="abs hero-photo" role="img" aria-label="Photo of a woman's neck and chest wearing a white bra"></div>

  <div class="abs product-thumb" style="left:1px;top:452px" role="img" aria-label="Serum dropper bottle with plum label"></div>
  <div class="abs product-thumb" style="left:118px;top:452px" role="img" aria-label="Breast cream jar with gold lid"></div>
  <div class="abs product-thumb" style="left:220px;top:452px" role="img" aria-label="Slim serum dropper bottle"></div>

  <h2 class="abs about-title">About Us</h2>
  <p class="abs about-text">Velvet Lotus curates organic infused products where holistic skin care meets a luxurious experience. Each ingredient is carefully selected; providing Ayurvedic herbs, rich minerals &amp; elements. Stimulating hydration and anti-oxidants to lift, firm and illuminate your skin. We believe in connecting with your inner mantra, stimulating higher vibrations, self-esteem, positive mind and soul. As a brand we work with our experts/suppliers of Ayurveda to ensure that our products meet the quality, wholesome healing that you need.</p>

  <div class="abs front-contact">
    <div>0000000000</div>
    <div>www.websiteaddress.com</div>
  </div>
</section>

<section class="rack-card rack-card--back">
  <svg class="card-shapes" viewBox="0 0 354 770" aria-hidden="true">
    <defs>
      <linearGradient id="goldEdge" x1="0" x2="1">
        <stop offset="0" stop-color="#e8c98a"/><stop offset=".5" stop-color="#a97c3e"/><stop offset="1" stop-color="#e8c98a"/>
      </linearGradient>
    </defs>
    <path d="M0,0 H354 V44 Q250,62 177,164 Q104,62 0,44 Z" fill="url(#goldEdge)"/>
    <path d="M0,0 H354 V56 Q250,72 177,158 Q104,72 0,56 Z" fill="var(--plum)"/>
    <path d="M30,672 Q177,648 324,672" stroke="url(#goldEdge)" stroke-width="3" fill="none"/>
    <path d="M0,688 Q177,660 354,688 V770 H0 Z" fill="var(--plum-light)"/>
  </svg>

  <h2 class="abs list-title">VELVET LOTUS<br>PRODUCT LIST</h2>

  <div class="abs product-frame" style="left:23px;top:182px" role="img" aria-label="Plum toner tube with gold cap"></div>
  <div class="abs product-info" style="top:222px">
    <h3 class="product-info__name">Velvet Lotus Firming and Lifting Breast Toner</h3>
    <p class="product-info__desc">Using all natural Ayurvedic herbs, our breast toner, prepares the area for maximum absorption, giving you the best results and the most invigorating treatment</p>
  </div>

  <div class="abs product-frame" style="left:23px;top:371px" role="img" aria-label="White cream jar with plum label and gold lid"></div>
  <div class="abs product-info" style="top:363px">
    <h3 class="product-info__name">Velvet Lotus Firming and Lifting Breast Cream</h3>
    <p class="product-info__desc">Using all natural Ayurvedic herbs, our breast cream helps enhance, tighten, and lift your breast</p>
  </div>

  <div class="abs product-frame" style="left:23px;top:512px" role="img" aria-label="Slim plum serum tube with gold cap"></div>
  <div class="abs product-info" style="top:524px">
    <h3 class="product-info__name">Velvet Lotus Firming and Toning Breast Serum</h3>
    <p class="product-info__desc">Using all natural Ayurvedic herbs, and a touch of 24k gold, our serum enhances the experience and quality of results when partnered with the Velvet Lotus Firming and Lifting Breast Cream providing an all-day boosting experience</p>
  </div>

  <div class="abs footer-brand"><span class="footer-brand__dot"></span><span class="footer-brand__name">VELVET LOTUS</span></div>
  <div class="abs footer-contact">
    <div class="footer-contact__cta">CALL US TODAY!</div>
    <div class="footer-contact__phone">0000000000</div>
    <div class="footer-contact__web">www.websiteaddress.com</div>
  </div>
</section>

</body>
</html>
```